Business card for medical clinic

I need an upmarket, modern medical/health business card for my clinic

Contact Information for Business Card

name, address, email, qr code

```html
<!DOCTYPE html>
<html lang="en">
<head>
<meta charset="utf-8">
<title>Meridian Care Partners – Business Card</title>
<link href="https://fonts.googleapis.com/css2?family=Montserrat:wght@400;500;600&display=swap" rel="stylesheet">
<style>
  :root {
    --backdrop: #3a3530;
    --card: #1d2a48;
    --card-edge: #182440;
    --accent: #2aa6e0;
    --brand-blue: #2f84b8;
    --text: #e9edf5;
    --mark-light: #3d5cb8;
    --white: #ffffff;
  }
  * { margin: 0; padding: 0; box-sizing: border-box; }
  html, body { width: 900px; height: 1200px; overflow: hidden; }
  body {
    background: var(--backdrop);
    font-family: "Montserrat", Arial, sans-serif;
    position: relative;
  }
  .card {
    position: absolute;
    background: var(--card);
    border-radius: 24px;
    overflow: hidden;
    box-shadow: 0 6px 18px rgba(0,0,0,.45);
  }
  .card--front { left: 80px; top: 130px; width: 742px; height: 442px; }
  .card--back  { left: 78px; top: 637px; width: 744px; height: 441px; }

  .brand-name {
    position: absolute;
    left: 35px; top: 70px;
    font-size: 25px;
    font-weight: 500;
    letter-spacing: 1px;
    color: var(--brand-blue);
    text-transform: uppercase;
  }
  .brand-decoration {
    position: absolute;
    left: 305px; top: 25px;
    width: 410px; height: 410px;
    border-radius: 50%;
    background: radial-gradient(circle at 20% 30%, rgba(61,92,184,.35), rgba(29,42,72,0) 70%);
  }
  .person { position: absolute; left: 38px; top: 186px; color: var(--text); }
  .person__name { font-size: 24px; font-weight: 600; color: var(--accent); line-height: 30px; }
  .person__role { font-size: 15px; font-weight: 400; margin-top: 2px; }
  .address { position: absolute; left: 41px; top: 262px; font-size: 16px; line-height: 20px; color: var(--text); }
  .contacts { position: absolute; left: 40px; top: 325px; list-style: none; }
  .contacts li {
    display: flex; align-items: center; gap: 11px;
    height: 31px; font-size: 15px; color: var(--text);
  }
  .contacts svg { width: 16px; height: 16px; fill: var(--accent); }

  .back-pattern {
    position: absolute; inset: 0;
    background: radial-gradient(ellipse at 0% 0%, rgba(61,92,184,.55) 0%, rgba(61,92,184,.15) 40%, rgba(29,42,72,0) 65%);
  }
  .back-brand {
    position: absolute; left: 354px; top: 270px;
    display: flex; align-items: center; gap: 12px;
  }
  .back-brand__circle {
    width: 58px; height: 58px; border-radius: 50%;
    border: 3px solid var(--white);
  }
  .back-brand__name {
    font-size: 19px; font-weight: 500; letter-spacing: .5px;
    color: var(--white); text-transform: uppercase;
  }
</style>
</head>
<body>
  <section class="card card--front">
    <div class="brand-name">Meridian Care</div>
    <div class="brand-decoration" role="img" aria-label="Large faint brand mark decoration"></div>
    <div class="person">
      <div class="person__name">Daniel Harper</div>
      <div class="person__role">Managing Director</div>
    </div>
    <div class="address">48 Cedar Ridge Lane<br>Clinton, MS 39056</div>
    <ul class="contacts">
      <li>
        <svg viewBox="0 0 24 24" aria-hidden="true"><path d="M6.6 10.8a15.1 15.1 0 0 0 6.6 6.6l2.2-2.2a1 1 0 0 1 1-.25 11.4 11.4 0 0 0 3.6.57 1 1 0 0 1 1 1V20a1 1 0 0 1-1 1A17 17 0 0 1 3 4a1 1 0 0 1 1-1h3.5a1 1 0 0 1 1 1c0 1.25.2 2.45.57 3.57a1 1 0 0 1-.25 1z"/></svg>
        555.214.7730
      </li>
      <li>
        <svg viewBox="0 0 24 24" aria-hidden="true"><path d="M2 5h20v14H2z" opacity=".0"/><path d="M3 5h18a1 1 0 0 1 1 1v.4l-10 6-10-6V6a1 1 0 0 1 1-1zm-1 3.7 10 6 10-6V18a1 1 0 0 1-1 1H3a1 1 0 0 1-1-1z"/></svg>
        hello@meridiancare.com
      </li>
      <li>
        <svg viewBox="0 0 24 24" aria-hidden="true"><path d="M12 2a10 10 0 1 0 0 20 10 10 0 0 0 0-20zm6.9 6h-3a15.6 15.6 0 0 0-1.3-3.9A8 8 0 0 1 18.9 8zM12 4c.8 1.1 1.5 2.5 1.9 4h-3.8c.4-1.5 1.1-2.9 1.9-4zM4.3 14a8.2 8.2 0 0 1 0-4h3.4a16.5 16.5 0 0 0 0 4zm.8 2h3a15.6 15.6 0 0 0 1.3 3.9A8 8 0 0 1 5.1 16zm3-8h-3a8 8 0 0 1 4.3-3.9A15.6 15.6 0 0 0 8.1 8zM12 20c-.8-1.1-1.5-2.5-1.9-4h3.8c-.4 1.5-1.1 2.9-1.9 4zm2.3-6H9.7a14.7 14.7 0 0 1 0-4h4.6a14.7 14.7 0 0 1 0 4zm.3 5.9a15.6 15.6 0 0 0 1.3-3.9h3a8 8 0 0 1-4.3 3.9zm1.7-5.9a16.5 16.5 0 0 0 0-4h3.4a8.2 8.2 0 0 1 0 4z"/></svg>
        www.meridiancare.com
      </li>
    </ul>
  </section>

  <section class="card card--back">
    <div class="back-pattern" role="img" aria-label="Repeating brand mark pattern fading from blue to navy"></div>
    <div class="back-brand">
      <span class="back-brand__circle"></span>
      <span class="back-brand__name">Meridian Care</span>
    </div>
  </section>
</body>
</html>
```